professional looking data specialist website

I've recently had a new logo designed and I'm now looking to get a professional looking website built. This is for a new company that specialises in data. We look to support companies with business intelligence, report modelling, data governance to new european legislation (GDPR). We are offer consultancy or we can attend site and complete work when required. Our target arket is united kingdom wide and we are specifically aiming at small to medium sized companies.

Target Market(s)

small to medium enterprise companies from all industries

Industry/Entity Type

Professional Service

Coding

Coded - Design and coding required

Number of Pages Required

4 page

Font styles to use
Sans Serif

Colors

Designer to choose colors to be used in the design.

Requirements
Must have
• Professional look including the company logo, need to have ability to request more information from us so needs a inquiries page, seperate pages for the different offerings, data governance, report modelling, business intelligence implementation, data protection
Nice to have
• any website interaction, animation, etc
Should not have
• too many colours, too busy pages, must look professional

```html
<!DOCTYPE html>
<html lang="en">
<head>
<meta charset="utf-8">
<title>Tarnvey Insight Ltd</title>
<link href="https://fonts.googleapis.com/css2?family=Ubuntu:wght@400;500;700&family=Arimo:wght@400&display=swap" rel="stylesheet">
<style>
:root{
  --blue:#1a6fc0;
  --ink:#3d3d3d;
  --muted:#555;
  --rule:#c8c8c8;
  --footer:#2b2b2b;
  --footer-line:#363636;
  --white:#fff;
}
*{margin:0;padding:0;box-sizing:border-box}
html,body{width:776px;height:1200px;overflow:hidden;background:var(--white)}
body{position:relative;font-family:"Ubuntu",sans-serif;color:var(--ink)}
.abs{position:absolute}

.top-rule{left:0;top:0;width:776px;height:2px;background:var(--blue)}
.header{left:0;top:2px;width:776px;height:85px;background:var(--white)}
.brand{left:52px;top:46px;display:flex;align-items:center;gap:8px;font-size:21px;font-weight:500;color:var(--blue);white-space:nowrap}
.brand-mark{width:16px;height:16px;background:var(--blue)}
.phone{left:498px;top:14px;display:flex;align-items:center;gap:5px;font-size:12px;color:var(--ink)}
.phone-box{width:20px;height:20px;border:1px solid #999;border-radius:3px;display:flex;align-items:center;justify-content:center}
.email-top{left:630px;top:18px;font-size:8.5px;color:var(--muted)}
.nav{left:404px;top:64px;display:flex;font-size:11px;color:var(--ink)}
.nav a{color:inherit;text-decoration:none;padding:0 18px;border-right:1px solid #ddd;line-height:11px}
.nav a:last-child{border-right:0;padding-right:0}
.nav a.active{color:var(--blue);font-weight:500;padding-left:16px}

.hero{left:0;top:87px;width:776px;height:324px;background:linear-gradient(90deg,#6d6d6d 0%,#9a9a9a 40%,#8a8a8a 100%)}
.hero-photo{left:350px;top:87px;width:426px;height:324px;background:radial-gradient(ellipse at 55% 55%,#4d8fb8 0%,#2e3e4c 45%,#1a1c20 80%)}
.hero-title{left:58px;top:222px;width:270px;font-size:17px;line-height:26px;font-weight:500;color:var(--white);text-shadow:1px 1px 3px rgba(0,0,0,.55)}
.hero-btn{left:64px;top:328px;width:92px;height:22px;background:var(--blue);color:var(--white);font-size:10px;font-weight:500;display:flex;align-items:center;justify-content:space-between;padding:0 5px 0 2px}
.arrow{top:218px;width:29px;height:24px;background:rgba(30,30,30,.85);display:flex;align-items:center;justify-content:center}
.arrow.prev{left:0}
.arrow.next{left:747px}
.hero-base{left:0;top:410px;width:776px;height:2px;background:#bbb}

.section-title{left:0;width:776px;text-align:center;font-size:21px;font-weight:500;color:var(--ink)}
.section-title span{color:var(--blue)}
.title-rule{left:363px;width:50px;height:1px;background:var(--rule)}

.card{top:508px;width:158px;height:136px;border:3px solid var(--rule);border-radius:6px}
.card.active{border-color:var(--blue)}
.card-img{position:absolute;left:5px;top:5px;width:142px;height:121px}
.card-label{top:651px;width:158px;text-align:center;font-size:13.5px;line-height:18px;font-weight:500;color:var(--ink)}
.card-label.active{color:var(--blue)}

.welcome-text{left:63px;top:802px;width:650px;text-align:center;font-family:"Arimo",sans-serif;font-size:9.4px;line-height:14.8px;color:#333}
.read-more{left:345px;top:873px;width:81px;height:23px;background:#8d8d8d;color:var(--white);font-size:10px;font-weight:500;display:flex;align-items:center;justify-content:space-between;padding:0 6px 0 8px}

.footer{left:0;top:930px;width:776px;height:241px;background:var(--footer)}
.footer-col-rule{top:1000px;width:1px;height:130px;background:var(--footer-line)}
.footer h3{position:absolute;font-size:14px;font-weight:500;color:var(--white)}
.field{left:53px;width:196px;height:18px;border:1px solid #9a9a9a;border-radius:2px;font-size:8px;color:var(--white);padding:3px 7px}
.send{left:53px;top:1125px;width:64px;height:20px;background:var(--blue);color:var(--white);font-size:9.5px;font-weight:500;display:flex;align-items:center;justify-content:center}
.map{left:309px;top:1003px;width:196px;height:118px;background:linear-gradient(135deg,#e9e4d6 0%,#b9d3e8 45%,#d9e4cc 75%,#e8e2d2 100%)}
.contact-item{left:565px;display:flex;gap:7px;font-size:8.6px;line-height:12px;color:var(--white)}
.contact-item svg{flex:none;margin-top:1px}

.copyright{left:0;top:1171px;width:776px;height:29px;background:var(--blue);color:var(--white);font-size:9.5px;font-weight:500;display:flex;align-items:center;justify-content:center}
</style>
</head>
<body>

<div class="abs top-rule"></div>
<header class="abs header"></header>
<div class="abs brand"><span class="brand-mark"></span>Tarnvey Insight Ltd</div>
<div class="abs phone">
  <span class="phone-box"><svg width="11" height="11" viewBox="0 0 24 24"><path fill="#1a6fc0" d="M6.6 10.8c1.4 2.8 3.8 5.1 6.6 6.6l2.2-2.2c.3-.3.7-.4 1-.2 1.1.4 2.3.6 3.6.6.6 0 1 .4 1 1V20c0 .6-.4 1-1 1C10.6 21 3 13.4 3 4c0-.6.4-1 1-1h3.5c.6 0 1 .4 1 1 0 1.3.2 2.5.6 3.6.1.3 0 .7-.2 1z"/></svg></span>
  (123)-555-0147
</div>
<div class="abs email-top">info@tarnveyinsight.com</div>
<nav class="abs nav">
  <a class="active" href="#">Home</a>
  <a href="#">About Us</a>
  <a href="#">Services</a>
  <a href="#">Contact Us</a>
</nav>

<section class="abs hero"></section>
<div class="abs hero-photo" role="img" aria-label="Businessman holding a tablet with a glowing world map, globe and data icons"></div>
<h1 class="abs hero-title">Offering Consultancy Services From Small To Medium EnterprisesCompanies To All Industries In The UK</h1>
<a class="abs hero-btn">Call Us Today<svg width="8" height="10" viewBox="0 0 8 10"><path d="M2 1l4 4-4 4" stroke="#fff" stroke-width="2" fill="none"/></svg></a>
<div class="abs arrow prev"><svg width="8" height="10" viewBox="0 0 8 10"><path d="M6 1L2 5l4 4" stroke="#fff" stroke-width="2" fill="none"/></svg></div>
<div class="abs arrow next"><svg width="8" height="10" viewBox="0 0 8 10"><path d="M2 1l4 4-4 4" stroke="#fff" stroke-width="2" fill="none"/></svg></div>
<div class="abs hero-base"></div>

<h2 class="abs section-title" style="top:440px">Our <span>Services</span></h2>
<div class="abs title-rule" style="top:477px"></div>

<div class="abs card active" style="left:72px"><div class="card-img" role="img" aria-label="Hand holding glowing data charts" style="background:linear-gradient(160deg,#2b3a8c,#141b4a 60%,#5a5fd0)"></div></div>
<div class="abs card" style="left:243px"><div class="card-img" role="img" aria-label="Tablet showing business charts on a desk" style="background:linear-gradient(160deg,#c9ecfb,#5cc3ef 60%,#e6f6fd)"></div></div>
<div class="abs card" style="left:414px"><div class="card-img" role="img" aria-label="Analyst working at a computer with reports" style="background:linear-gradient(160deg,#f3f3f3,#d6d8dc 60%,#eef0f2)"></div></div>
<div class="abs card" style="left:586px"><div class="card-img" role="img" aria-label="Padlock on a circuit board" style="background:radial-gradient(circle at 50% 45%,#a9d8f5,#2a6fb0 45%,#10284d)"></div></div>

<div class="abs card-label active" style="left:72px">Data<br>Governance</div>
<div class="abs card-label" style="left:243px">Business Intelligence<br>Implementation</div>
<div class="abs card-label" style="left:414px">Report<br>Modeling</div>
<div class="abs card-label" style="left:586px">Data<br>Protection</div>

<h2 class="abs section-title" style="top:750px">Welcome To <span>Tarnvey Insight</span> Ltd</h2>
<div class="abs title-rule" style="top:787px"></div>
<p class="abs welcome-text">Lorem ipsum dolor sit amet, consectetuer adipiscing elit, sed diam nonummy nibh euismod tincidunt ut laoreet dolore magna aliquam erat volutpat. Ut wisi enim ad minim veniam, quis nostrud exerci tation ullamcorper suscipit lobortis nisl ut aliquip ex ea commodo consequat. Duis autem vel eum iriure dolor in hendrerit in vulputate velit esse molestie consequat, vel illum dolore eu feugiat nulla facilisis at vero eros et accumsan et iusto odio dignissim qui blandit praesent luptatum zzril delenit augue duis dolore te feugait nulla facilisi.</p>
<a class="abs read-more">Read More<svg width="8" height="10" viewBox="0 0 8 10"><path d="M2 1l4 4-4 4" stroke="#fff" stroke-width="2" fill="none"/></svg></a>

<footer class="abs footer">
  <h3 style="left:55px;top:43px">Quick Inquiry</h3>
  <h3 style="left:308px;top:41px">Location Map</h3>
  <h3 style="left:572px;top:53px">Contact Details</h3>
</footer>
<div class="abs footer-col-rule" style="left:276px"></div>
<div class="abs footer-col-rule" style="left:530px"></div>

<div class="abs field" style="top:1002px">Name</div>
<div class="abs field" style="top:1024px">Email</div>
<div class="abs field" style="top:1045px">Subject</div>
<div class="abs field" style="top:1066px;height:52px">Message</div>
<div class="abs send">SEND</div>

<div class="abs map" role="img" aria-label="Street map of the office location with a marker"></div>

<div class="abs contact-item" style="top:1001px">
  <svg width="9" height="11" viewBox="0 0 12 16"><path fill="#1a6fc0" d="M6 0C2.7 0 0 2.6 0 5.9 0 10 6 16 6 16s6-6 6-10.1C12 2.6 9.3 0 6 0zm0 8.2a2.3 2.3 0 110-4.6 2.3 2.3 0 010 4.6z"/></svg>
  <span style="margin-left:4px">Loren ipsum dolor sit amet mbert<br>Hillcrest Way, London SE1 9ZZ.</span>
</div>
<div class="abs contact-item" style="top:1038px">
  <svg width="11" height="11" viewBox="0 0 24 24"><path fill="#1a6fc0" d="M6.6 10.8c1.4 2.8 3.8 5.1 6.6 6.6l2.2-2.2c.3-.3.7-.4 1-.2 1.1.4 2.3.6 3.6.6.6 0 1 .4 1 1V20c0 .6-.4 1-1 1C10.6 21 3 13.4 3 4c0-.6.4-1 1-1h3.5c.6 0 1 .4 1 1 0 1.3.2 2.5.6 3.6.1.3 0 .7-.2 1z"/></svg>
  <span>123-555-0147</span>
</div>
<div class="abs contact-item" style="top:1064px">
  <svg width="11" height="11" viewBox="0 0 12 12"><rect x="3" y="0" width="6" height="3" fill="#1a6fc0"/><rect x="0" y="3" width="12" height="6" rx="1" fill="#1a6fc0"/><rect x="3" y="8" width="6" height="4" fill="#1a6fc0"/></svg>
  <span>123-555-0147</span>
</div>
<div class="abs contact-item" style="top:1091px">
  <svg width="11" height="9" viewBox="0 0 12 9"><rect width="12" height="9" fill="#1a6fc0"/><path d="M0 0l6 5 6-5" stroke="#2b2b2b" stroke-width="1.2" fill="none"/></svg>
  <span>info@tarnveyinsight.com</span>
</div>

<div class="abs copyright">Copyright © 2017 Tarnvey Insight Ltd . All Right Reserved</div>

</body>
</html>
```